Proposal Template Design

We are looking to have our proposal templates redesigned. attached are examples of what we have been using. as well as our current logo

```html
<!DOCTYPE html>
<html lang="en">
<head>
<meta charset="utf-8">
<title>Proposal Template – Page Spread</title>
<link href="https://fonts.googleapis.com/css2?family=Arimo:wght@400;700&display=swap" rel="stylesheet">
<style>
:root{
  --bg:#e6ecf8;
  --navy:#0c1f5e;
  --stripe:#1a73c9;
  --heading:#1557a8;
  --link:#1f6fd1;
  --panel:#cfe5fb;
  --team:#2a9ad6;
  --ink:#111;
  --muted:#777;
  --paper:#fff;
}
*{margin:0;padding:0;box-sizing:border-box}
html,body{width:1200px;height:1200px;overflow:hidden;background:var(--bg);font-family:"Arimo",Arial,sans-serif;color:var(--ink)}
.spread{position:relative;width:1200px;height:1200px}
.page{position:absolute;width:265px;height:343px;background:var(--paper);overflow:hidden;box-shadow:0 1px 3px rgba(20,40,90,.12)}
.c1{left:176px}.c2{left:473px}.c3{left:770px}
.r1{top:61px}.r2{top:432px}.r3{top:801px}
.abs{position:absolute}

.doc-bar{position:absolute;top:14px;left:25px;width:217px;height:7px;background:var(--navy);color:#fff;font-size:3.2px;line-height:7px;padding:0 4px;letter-spacing:.1px}
.doc-bar.accent-right{border-right:3px solid var(--stripe)}
.doc-bar.accent-left{border-left:3px solid var(--stripe);text-align:right}
.foot-line{position:absolute;top:323px;left:25px;width:215px;height:2px;background:var(--navy)}
.foot-text{position:absolute;top:328px;left:27px;width:211px;font-size:3.2px;color:var(--muted);display:flex;justify-content:space-between}

.copy p{font-size:3.8px;line-height:1.42;margin-bottom:3px}
.copy.small p{font-size:3.6px}
.section-title{position:absolute;left:25px;width:215px;font-weight:700;color:var(--heading);font-size:15px;line-height:1;padding-bottom:2px;border-bottom:1px solid var(--heading)}
.sub-title{font-weight:700;color:var(--heading);font-size:8.5px;margin:4px 0 4px}
.sub-plain{font-weight:700;font-size:5.5px;margin:3px 0 3px}

.smoke{background:
  radial-gradient(ellipse 60% 22% at 45% 52%, rgba(110,170,205,.85), rgba(40,90,120,.35) 55%, transparent 80%),
  radial-gradient(ellipse 50% 30% at 20% 85%, rgba(90,20,30,.5), transparent 70%),
  linear-gradient(180deg,#050507,#0b0d12 60%,#120a0e)}
.portrait{background:radial-gradient(ellipse 40% 45% at 50% 40%, #d8c2b0, #bfb6ae 55%, #9d9d9d),linear-gradient(#a9a9a9,#cfcfcf)}

/* cover */
.cover-panel{left:0;top:0;width:115px;height:343px;background:var(--navy)}
.cover-stripe{left:115px;top:0;width:9px;height:343px;background:var(--stripe)}
.cover-title{left:22px;top:72px;color:#fff;font-weight:700;font-size:27px;line-height:1.1;width:83px;padding-bottom:4px;border-bottom:1.5px solid #fff}
.cover-copy{left:22px;top:143px;width:84px;color:#fff}
.cover-copy p{font-size:3.6px;line-height:1.42;margin-bottom:3px}
.cover-box{left:22px;top:282px;width:73px;height:12px;border:.8px solid #fff;color:#fff;font-size:3.6px;padding:2px 3px}
.brand{display:flex;align-items:center;gap:4px;color:var(--navy);font-weight:700;font-size:8px;line-height:1.05}
.brand .mark{width:9px;height:9px;background:var(--stripe);flex:none}

/* title page */
.main-title{left:36px;top:174px;font-weight:700;font-size:24px;line-height:1;width:157px;padding-bottom:2px;border-bottom:1.5px solid var(--navy)}

/* toc */
.toc{left:25px;top:146px;width:215px}
.toc-row{display:flex;align-items:baseline;font-size:5px;height:9.2px}
.toc-row .dots{flex:1;border-bottom:.6px dotted #555;margin:0 1px;transform:translateY(-1px)}
.toc-row.main{color:var(--link)}
.toc-row.minor{font-weight:700;font-size:4.4px}

/* about */
.two-col{display:grid;grid-template-columns:1fr 1fr;gap:8px}

/* heading panel */
.panel{left:25px;top:30px;width:215px;height:145px;background:var(--panel);padding:9px 9px}
.panel .section-title{position:static;width:auto;margin-bottom:4px}

/* team */
.member{position:absolute;top:77px;width:56px}
.member .portrait{height:82px}
.member .name{color:var(--team);font-weight:700;font-size:6px;margin-top:4px}
.member .role{color:var(--team);font-size:4px;margin:1px 0 5px}
.member p{font-size:3.6px;line-height:1.42;margin-bottom:3px}

/* table */
.data-table{width:215px;border-collapse:collapse;border-top:.7px solid var(--heading);border-bottom:.7px solid var(--heading)}
.data-table th{color:var(--heading);font-size:5px;text-align:left;padding:2px 3px;height:8px}
.data-table td{height:11.5px}
.data-table tr.band td{background:var(--panel)}

/* back */
.back-strip{left:0;top:0;width:17px;height:343px;background:var(--navy)}
.contact{left:40px;top:265px;font-size:4px}
.contact li{list-style:none;display:flex;align-items:center;gap:4px;height:9.5px}
.contact svg{width:5px;height:5px}
.back-rule{left:158px;top:254px;width:1px;height:51px;background:var(--navy)}
</style>
</head>
<body>
<main class="spread">

  <!-- Cover -->
  <section class="page c1 r1">
    <div class="abs cover-panel"></div>
    <div class="abs cover-stripe"></div>
    <div class="abs brand" style="left:150px;top:24px"><span class="mark"></span><span>Northfield<br>Insulation</span></div>
    <div class="abs smoke" style="left:133px;top:78px;width:132px;height:224px" role="img" aria-label="Dark photograph of blue smoke"></div>
    <h1 class="abs cover-title">MAIN TITLE</h1>
    <div class="abs cover-copy">
      <p>Lorem ipsum dolor sit amet, consectetuer adipiscing elit. Maecenas porttitor congue massa. Fusce posuere, magna sed pulvinar ultricies, purus lectus malesuada libero, sit amet commodo magna eros quis urna.</p>
      <p>Nunc viverra imperdiet enim. Fusce est. Vivamus a tellus.</p>
    </div>
    <div class="abs cover-box">Some Text Here</div>
  </section>

  <!-- Title page -->
  <section class="page c2 r1">
    <div class="doc-bar accent-right">[DOCUMENT TITLE]</div>
    <h2 class="abs main-title">MAIN TITLE</h2>
    <div class="abs copy" style="left:37px;top:208px;width:183px">
      <p>Lorem ipsum dolor sit amet, consectetuer adipiscing elit. Maecenas porttitor congue massa. Fusce posuere, magna sed pulvinar ultricies, purus lectus malesuada libero, sit amet commodo magna eros quis urna.</p>
      <p>Nunc viverra imperdiet enim. Fusce est. Vivamus a tellus. Lorem ipsum dolor sit amet, consectetuer adipiscing elit. Maecenas porttitor congue massa. Fusce posuere, magna sed pulvinar ultricies, purus lectus malesuada libero, sit amet commodo magna eros quis urna.</p>
      <p>Nunc viverra imperdiet enim. Fusce est. Vivamus a tellus.</p>
    </div>
    <div class="foot-line"></div>
    <div class="foot-text"><span>NFI</span><span>2</span></div>
  </section>

  <!-- Table of contents -->
  <section class="page c3 r1">
    <div class="doc-bar accent-left">[DOCUMENT TITLE]</div>
    <h2 class="section-title" style="top:118px">Table of Contents</h2>
    <nav class="abs toc">
      <div class="toc-row main"><span>About Us</span><span class="dots"></span><span>4</span></div>
      <div class="toc-row main"><span>Some Heading Here</span><span class="dots"></span><span>5</span></div>
      <div class="toc-row minor"><span>Sub Heading 1</span><span class="dots"></span><span>5</span></div>
      <div class="toc-row minor"><span>Sub Heading 1</span><span class="dots"></span><span>5</span></div>
      <div class="toc-row main"><span>Image With Text</span><span class="dots"></span><span>6</span></div>
      <div class="toc-row main"><span>Team Style</span><span class="dots"></span><span>7</span></div>
      <div class="toc-row main"><span>Full Page Text</span><span class="dots"></span><span>8</span></div>
      <div class="toc-row minor"><span>Sub heading 1</span><span class="dots"></span><span>8</span></div>
      <div class="toc-row minor"><span>Sub heading 2</span><span class="dots"></span><span>8</span></div>
      <div class="toc-row minor"><span>Table</span><span class="dots"></span><span>8</span></div>
    </nav>
    <div class="foot-line"></div>
    <div class="foot-text"><span>3</span><span>NFI</span></div>
  </section>

  <!-- About us -->
  <section class="page c1 r2">
    <div class="doc-bar accent-right">[DOCUMENT TITLE]</div>
    <div class="abs smoke" style="left:25px;top:31px;width:218px;height:143px" role="img" aria-label="Dark photograph of blue smoke"></div>
    <h2 class="section-title" style="top:182px;width:215px">About Us</h2>
    <div class="abs copy small two-col" style="left:25px;top:204px;width:215px">
      <div>
        <p>Lorem ipsum dolor sit amet, consectetuer adipiscing elit. Maecenas porttitor congue massa. Fusce posuere, magna sed pulvinar ultricies, purus lectus malesuada libero, sit amet commodo magna eros quis urna.</p>
        <p>Nunc viverra imperdiet enim. Fusce est. Vivamus a tellus. Lorem ipsum dolor sit amet, consectetuer adipiscing elit. Maecenas porttitor congue massa. Fusce posuere, magna sed pulvinar ultricies, purus lectus malesuada libero, sit amet commodo magna eros quis urna.</p>
        <p>Nunc viverra imperdiet enim. Fusce est. Vivamus a tellus.</p>
      </div>
      <div>
        <p>Lorem ipsum dolor sit amet, consectetuer adipiscing elit. Maecenas porttitor congue massa. Fusce posuere, magna sed pulvinar ultricies, purus lectus malesuada libero, sit amet commodo magna eros quis urna.</p>
        <p>Nunc viverra imperdiet enim. Fusce est. Vivamus a tellus. Lorem ipsum dolor sit amet, consectetuer adipiscing elit. Maecenas porttitor congue massa. Fusce posuere, magna sed pulvinar ultricies, purus lectus malesuada libero, sit amet commodo magna eros quis urna.</p>
        <p>Nunc viverra imperdiet enim. Fusce est. Vivamus a tellus.</p>
      </div>
    </div>
    <div class="foot-line"></div>
    <div class="foot-text"><span>NFI</span><span>4</span></div>
  </section>

  <!-- Heading panel page -->
  <section class="page c2 r2">
    <div class="doc-bar accent-left">[DOCUMENT TITLE]</div>
    <div class="abs panel copy">
      <h2 class="section-title">Some Heading Here</h2>
      <p>Lorem ipsum dolor sit amet, consectetuer adipiscing elit. Maecenas porttitor congue massa. Fusce posuere, magna sed pulvinar ultricies, purus lectus malesuada libero, sit amet commodo magna eros quis urna.</p>
      <p>Nunc viverra imperdiet enim. Fusce est. Vivamus a tellus. Lorem ipsum dolor sit amet, consectetuer adipiscing elit. Maecenas porttitor congue massa. Fusce posuere, magna sed pulvinar ultricies, purus lectus malesuada libero, sit amet commodo magna eros quis urna.</p>
      <p>Nunc viverra imperdiet enim. Fusce est. Vivamus a tellus.</p>
      <p>Lorem ipsum dolor sit amet, consectetuer adipiscing elit. Maecenas porttitor congue massa. Fusce posuere, magna sed pulvinar ultricies, purus lectus malesuada libero, sit amet commodo magna eros quis urna.</p>
      <p>Nunc viverra imperdiet enim. Fusce est. Vivamus a tellus. Lorem ipsum dolor sit amet, consectetuer adipiscing elit. Maecenas porttitor congue massa. Fusce posuere, magna sed pulvinar ultricies, purus lectus malesuada libero, sit amet commodo magna eros quis urna.</p>
      <p>Nunc viverra imperdiet enim. Fusce est. Vivamus a tellus.</p>
    </div>
    <div class="abs copy" style="left:25px;top:180px;width:215px;height:134px;overflow:hidden">
      <h3 class="sub-title">Sub Heading 1</h3>
      <p>Lorem ipsum dolor sit amet, consectetuer adipiscing elit. Maecenas porttitor congue massa. Fusce posuere, magna sed pulvinar ultricies, purus lectus malesuada libero, sit amet commodo magna eros quis urna.</p>
      <p>Nunc viverra imperdiet enim. Fusce est. Vivamus a tellus. Lorem ipsum dolor sit amet, consectetuer adipiscing elit. Maecenas porttitor congue massa. Fusce posuere, magna sed pulvinar ultricies, purus lectus malesuada libero, sit amet commodo magna eros quis urna.</p>
      <p>Nunc viverra imperdiet enim. Fusce est. Vivamus a tellus.</p>
      <p>Lorem ipsum dolor sit amet, consectetuer adipiscing elit. Maecenas porttitor congue massa. Fusce posuere, magna sed pulvinar ultricies, purus lectus malesuada libero, sit amet commodo magna eros quis urna.</p>
      <h3 class="sub-title">Sub Heading 1</h3>
      <p>Lorem ipsum dolor sit amet, consectetuer adipiscing elit. Maecenas porttitor congue massa. Fusce posuere, magna sed pulvinar ultricies, purus lectus malesuada libero, sit amet commodo magna eros quis urna.</p>
      <p>Nunc viverra imperdiet enim. Fusce est. Vivamus a tellus. Lorem ipsum dolor sit amet, consectetuer</p>
    </div>
    <div class="foot-line"></div>
    <div class="foot-text"><span>5</span><span>NFI</span></div>
  </section>

  <!-- Image with text -->
  <section class="page c3 r2">
    <div class="doc-bar accent-right">[DOCUMENT TITLE]</div>
    <h2 class="section-title" style="top:34px">Image With Text</h2>
    <div class="abs smoke" style="left:0;top:68px;width:146px;height:242px" role="img" aria-label="Dark photograph of blue smoke"></div>
    <div class="abs copy small" style="left:156px;top:65px;width:84px">
      <p>Lorem ipsum dolor sit amet, consectetuer adipiscing elit. Maecenas porttitor congue massa. Fusce posuere, magna sed pulvinar ultricies, purus lectus malesuada libero, sit amet commodo magna eros quis urna.</p>
      <p>Nunc viverra imperdiet enim. Fusce est. Vivamus a tellus. Lorem ipsum dolor sit amet, consectetuer adipiscing elit. Maecenas porttitor congue massa. Fusce posuere, magna sed pulvinar ultricies, purus lectus malesuada libero, sit amet commodo magna eros quis urna.</p>
      <p>Nunc viverra imperdiet enim. Fusce est. Vivamus a tellus.</p>
      <p>Lorem ipsum dolor sit amet, consectetuer adipiscing elit. Maecenas porttitor congue massa. Fusce posuere, magna sed pulvinar ultricies, purus lectus malesuada libero, sit amet commodo magna eros quis urna.</p>
      <p>Nunc viverra imperdiet enim. Fusce est. Vivamus a tellus. Lorem ipsum dolor sit amet, consectetuer adipiscing elit. Maecenas porttitor congue massa. Fusce posuere, magna sed pulvinar ultricies, purus lectus malesuada libero, sit amet commodo magna eros quis urna.</p>
      <p>Nunc viverra imperdiet enim. Fusce est. Vivamus a tellus.</p>
    </div>
    <div class="foot-line"></div>
    <div class="foot-text"><span>NFI</span><span>6</span></div>
  </section>

  <!-- Team -->
  <section class="page c1 r3">
    <div class="doc-bar accent-left">[DOCUMENT TITLE]</div>
    <h2 class="section-title" style="top:34px">Team Style</h2>
    <article class="member" style="left:34px">
      <div class="portrait" role="img" aria-label="Team member portrait photo"></div>
      <div class="name">Name Here</div><div class="role">Title here</div>
      <p>Lorem ipsum dolor sit amet, consectetuer adipiscing elit. Maecenas porttitor congue massa. Fusce posuere, magna sed pulvinar ultricies, purus lectus malesuada libero, sit amet commodo magna eros quis urna.</p>
      <p>Nunc viverra imperdiet enim. Fusce est. Vivamus a tellus. Lorem ipsum dolor sit amet, consectetuer adipiscing elit. Maecenas porttitor congue massa. Fusce posuere, magna sed pulvinar ultricies, purus lectus malesuada libero, sit amet commodo magna eros quis urna.</p>
    </article>
    <article class="member" style="left:106px">
      <div class="portrait" role="img" aria-label="Team member portrait photo"></div>
      <div class="name">Name Here</div><div class="role">Title here</div>
      <p>Lorem ipsum dolor sit amet, consectetuer adipiscing elit. Maecenas porttitor congue massa. Fusce posuere, magna sed pulvinar ultricies, purus lectus malesuada libero, sit amet commodo magna eros quis urna.</p>
      <p>Nunc viverra imperdiet enim. Fusce est. Vivamus a tellus. Lorem ipsum dolor sit amet, consectetuer adipiscing elit. Maecenas porttitor congue massa. Fusce posuere, magna sed pulvinar ultricies, purus lectus malesuada libero, sit amet commodo magna eros quis urna.</p>
    </article>
    <article class="member" style="left:176px">
      <div class="portrait" role="img" aria-label="Team member portrait photo"></div>
      <div class="name">Name Here</div><div class="role">Title here</div>
      <p>Lorem ipsum dolor sit amet, consectetuer adipiscing elit. Maecenas porttitor congue massa. Fusce posuere, magna sed pulvinar ultricies, purus lectus malesuada libero, sit amet commodo magna eros quis urna.</p>
      <p>Nunc viverra imperdiet enim. Fusce est. Vivamus a tellus. Lorem ipsum dolor sit amet, consectetuer adipiscing elit. Maecenas porttitor congue massa. Fusce posuere, magna sed pulvinar ultricies, purus lectus malesuada libero, sit amet commodo magna eros quis urna.</p>
    </article>
    <div class="foot-line"></div>
    <div class="foot-text"><span>7</span><span>NFI</span></div>
  </section>

  <!-- Full page text -->
  <section class="page c2 r3">
    <div class="doc-bar accent-right">[DOCUMENT TITLE]</div>
    <h2 class="section-title" style="top:34px">Full Page Text</h2>
    <div class="abs copy" style="left:25px;top:59px;width:215px">
      <p>Nunc viverra imperdiet enim. Fusce est. Vivamus a tellus. Lorem ipsum dolor sit amet, consectetuer adipiscing elit. Maecenas porttitor congue massa. Fusce posuere, magna sed pulvinar ultricies, purus lectus malesuada libero, sit amet commodo magna eros quis urna.</p>
      <p>Nunc viverra imperdiet enim. Fusce est. Vivamus a tellus.</p>
      <p>Lorem ipsum dolor sit amet, consectetuer adipiscing elit. Maecenas porttitor congue massa. Fusce posuere, magna sed pulvinar ultricies, purus lectus malesuada libero, sit amet commodo magna eros quis urna.</p>
      <h3 class="sub-title">Sub heading 1</h3>
      <p>Nunc viverra imperdiet enim. Fusce est. Vivamus a tellus. Lorem ipsum dolor sit amet, consectetuer adipiscing elit. Maecenas porttitor congue massa. Fusce posuere, magna sed pulvinar ultricies, purus lectus malesuada libero, sit amet commodo magna eros quis urna.</p>
      <p>Nunc viverra imperdiet enim. Fusce est. Vivamus a tellus.</p>
      <p>Lorem ipsum dolor sit amet, consectetuer adipiscing elit. Maecenas porttitor congue massa. Fusce posuere, magna sed pulvinar ultricies, purus lectus malesuada libero, sit amet commodo magna eros quis urna.</p>
      <h4 class="sub-plain">Sub heading 2</h4>
      <p>Nunc viverra imperdiet enim. Fusce est. Vivamus a tellus. Lorem ipsum dolor sit amet, consectetuer adipiscing elit. Maecenas porttitor congue massa. Fusce posuere, magna sed pulvinar ultricies, purus lectus malesuada libero, sit amet commodo magna eros quis urna.</p>
      <p>Nunc viverra imperdiet enim. Fusce est. Vivamus a tellus.</p>
      <p>Lorem ipsum dolor sit amet, consectetuer adipiscing elit. Maecenas porttitor congue massa. Fusce posuere, magna sed pulvinar ultricies, purus lectus malesuada libero, sit amet commodo magna eros quis urna.</p>
      <h4 class="sub-plain">Table</h4>
      <table class="data-table">
        <tr><th>Header</th><th>Header</th><th>Header</th><th>Header</th></tr>
        <tr class="band"><td></td><td></td><td></td><td></td></tr>
        <tr><td></td><td></td><td></td><td></td></tr>
        <tr class="band"><td></td><td></td><td></td><td></td></tr>
        <tr><td></td><td></td><td></td><td></td></tr>
      </table>
    </div>
    <div class="foot-line"></div>
    <div class="foot-text"><span>NFI</span><span>8</span></div>
  </section>

  <!-- Back cover -->
  <section class="page c3 r3">
    <div class="abs back-strip"></div>
    <ul class="abs contact">
      <li><svg viewBox="0 0 10 10"><circle cx="5" cy="5" r="5" fill="#bbb"/><path d="M5 2.2a2 2 0 0 1 2 2c0 1.5-2 3.6-2 3.6S3 5.7 3 4.2a2 2 0 0 1 2-2z" fill="#fff"/></svg>P.O Box 214, Alder Creek Ohio 44012</li>
      <li><svg viewBox="0 0 10 10"><circle cx="5" cy="5" r="5" fill="#bbb"/><path d="M3.2 2.6l1.1 1.2-.6.8c.4.8 1 1.4 1.8 1.8l.8-.6 1.2 1.1-.6.9c-2 0-4.4-2.4-4.4-4.4z" fill="#fff"/></svg>office@northfieldinsulation.com</li>
      <li><svg viewBox="0 0 10 10"><circle cx="5" cy="5" r="5" fill="#bbb"/><rect x="2.6" y="3.2" width="4.8" height="3.6" fill="#fff"/><path d="M2.6 3.2L5 5.2l2.4-2" stroke="#bbb" stroke-width=".6" fill="none"/></svg>555-014-2290</li>
    </ul>
    <div class="abs back-rule"></div>
    <div class="abs brand" style="left:168px;top:270px"><span class="mark"></span><span>Northfield<br>Insulation</span></div>
  </section>

</main>
</body>
</html>
```